Quillon Maison Wood Fired Pizza business card design

I have a logo and need an eye catching design that will get me noticed.
My business is wood fired pizza. I want a bold design that will make our customers remember us and the food that we serve. Work with the colors of our logo and texts. Maybe add designs that lend to what or how pizza is made using our wood fired oven?

Target Market(s)

Foodies!

Contact Information for Business Card

Quillon Maison Wood Fired Pizza
Our slogan is Fast. Fresh. Handcrafted
Catering for all events

Requirements
Must have
• Dana Porrick
Telephone 570 555 0183
website www.getquillon.example
Facebook @getquillonpizza maybe use the facebook logo next to it
Instagram getquillonpizza maybe use the instagram logo next to it
Catering for all events
Nice to have
• Maybe pizza peels, pizza cutters? Wood? Fired wood? Using our flame in the background?
Please work with different colored text so each sentence stands out? A themed color for facebook?
Maybe work with the colors within our logo?
Please try to use the our quillon font, but not a must have.

```html
<!DOCTYPE html>
<html lang="en">
<head>
<meta charset="utf-8">
<title>Quillon Maison Wood Fired Pizza — Business Card</title>
<link rel="stylesheet" href="https://fonts.googleapis.com/css2?family=Work+Sans:wght@400;500;700&display=swap">
<style>
  :root {
    --stage: #1c1d22;
    --card-white: #ffffff;
    --card-navy: #141826;
    --pattern-navy: #1d2336;
    --flame-red: #d0161b;
    --ember-orange: #f39322;
    --ink: #15161a;
  }
  * { margin: 0; padding: 0; box-sizing: border-box; }
  html, body {
    width: 1200px; height: 900px; overflow: hidden;
    background: var(--stage);
    font-family: "Work Sans", Arial, sans-serif;
  }
  .card-slot {
    position: absolute; left: 270px;
    width: 660px; height: 378px;
  }
  .card-slot.front { top: 40px; }
  .card-slot.back { top: 478px; }
  .card {
    position: absolute; left: 0; top: 0;
    width: 1000px; height: 572px;
    transform: scale(0.66); transform-origin: top left;
    border-radius: 34px; overflow: hidden;
    box-shadow: 0 20px 50px rgba(0,0,0,.55);
  }
  .card-front { background: var(--card-white); }
  .card-back { background: var(--card-navy); }
  .card-shapes { position: absolute; inset: 0; }
  .brand {
    position: absolute; left: 92px; top: 120px;
    display: flex; align-items: center; gap: 14px;
  }
  .brand-dot {
    width: 44px; height: 44px; border-radius: 50%;
    background: var(--flame-red);
  }
  .brand-name {
    font-weight: 700; font-size: 38px; letter-spacing: 1px;
    color: var(--ink); text-transform: uppercase;
  }
  .slogan {
    position: absolute; left: 560px; top: 112px;
    font-size: 24px; font-weight: 500; letter-spacing: 1.5px;
    color: var(--ember-orange); text-transform: uppercase;
  }
  .catering {
    position: absolute; left: 48px; top: 362px;
    font-size: 22px; font-weight: 500; letter-spacing: 1.5px;
    color: var(--ember-orange); text-transform: uppercase;
  }
  .contact-block {
    position: absolute; right: 200px; top: 380px;
    text-align: right;
  }
  .person-name {
    font-size: 30px; font-weight: 500; letter-spacing: 1px;
    color: var(--flame-red); text-transform: uppercase; line-height: 1;
  }
  .person-role {
    font-size: 18px; line-height: 22px; color: var(--ember-orange); margin-top: 2px;
  }
  .contact-list { list-style: none; margin-top: 4px; }
  .contact-list li {
    display: flex; justify-content: flex-end; align-items: center; gap: 10px;
    font-size: 18px; line-height: 23px; color: var(--ember-orange);
  }
  .contact-icon { width: 15px; height: 15px; flex: none; }
  .social-mark {
    width: 13px; height: 13px; border-radius: 50%;
    background: var(--flame-red); flex: none; margin: 0 1px;
  }
  .back-pattern {
    position: absolute; inset: 0;
    background: linear-gradient(135deg, var(--card-navy), var(--pattern-navy) 50%, var(--card-navy));
  }
  .back-brand {
    position: absolute; left: 610px; top: 150px;
    font-size: 30px; font-weight: 700; letter-spacing: 1px;
    color: var(--flame-red); text-transform: uppercase;
  }
</style>
</head>
<body>
  <div class="card-slot front">
    <article class="card card-front">
      <svg class="card-shapes" viewBox="0 0 1000 572" width="1000" height="572" aria-hidden="true">
        <path d="M0,190 C90,330 260,330 520,318 C300,322 130,330 0,220 Z" fill="var(--flame-red)"/>
        <path d="M0,222 C110,360 300,340 560,336 C760,332 880,352 1000,458 L1000,470 C880,372 760,352 560,354 C300,358 120,380 0,250 Z" fill="var(--ember-orange)"/>
        <path d="M0,256 C120,392 300,370 560,366 C760,362 880,382 1000,478 L1000,572 L0,572 Z" fill="var(--card-navy)"/>
      </svg>

      <div class="brand">
        <span class="brand-dot"></span>
        <span class="brand-name">Quillon Maison</span>
      </div>
      <p class="slogan">Fast. Fresh. Handcrafted</p>
      <p class="catering">Catering for all events</p>

      <div class="contact-block">
        <p class="person-name">Dana Porrick</p>
        <p class="person-role">Founder</p>
        <ul class="contact-list">
          <li>getquillonpizza <span class="social-mark"></span></li>
          <li>getquillonpizza <span class="social-mark"></span></li>
          <li>570 555 0183
            <svg class="contact-icon" viewBox="0 0 16 16"><path d="M3 1l3 3-1.5 2a9 9 0 0 0 5.5 5.5L12 10l3 3-2 2C7 15 1 9 1 3z" fill="var(--flame-red)"/></svg>
          </li>
          <li>info@getquillon.example
            <svg class="contact-icon" viewBox="0 0 16 16"><rect x="1" y="3" width="14" height="10" fill="none" stroke="var(--flame-red)" stroke-width="1.6"/><path d="M1 3l7 6 7-6" fill="none" stroke="var(--flame-red)" stroke-width="1.6"/></svg>
          </li>
          <li>www.getquillon.example
            <svg class="contact-icon" viewBox="0 0 16 16"><g fill="none" stroke="var(--flame-red)" stroke-width="1.4"><circle cx="8" cy="8" r="6.5"/><ellipse cx="8" cy="8" rx="3" ry="6.5"/><path d="M1.5 8h13"/></g></svg>
          </li>
        </ul>
      </div>
    </article>
  </div>

  <div class="card-slot back">
    <article class="card card-back">
      <div class="back-pattern" role="img" aria-label="Tonal embossed flame pattern repeated across the navy card back"></div>
      <p class="back-brand">Quillon Maison</p>
    </article>
  </div>
</body>
</html>
```